Local Electrical company need some kick ass business cards

In need of some in your face design business cards for a family owned electrical service company in Edmonton, Alberta Canada. We provide reliable and trustworthy electrical service for commercial and residential work in the Edmonton and area. We have been in business for 25 years.

Target Market(s)

Residential and commercial electrical

Industry/Entity Type

Business

Contact Information for Business Card

Your welcome to change and modify the brightway electric logo. please include the lightbulb! Our Colours are black and green please stay with that.
Please include a name phone number and address on the card
phone number - 780-318-5062
#22, 418 Maple Cres, St.Albert, Alberta.
Two things that need to be on the card.
"your friendly neighborhood electrictrician"
Commercial & residential electrical repair and service

Colors
9bcb3c

Requirements
Must have
• Light bulb guy Attached
• "your friendly neighborhood electrictrician"
• Commercial & residential electrical repair and service
• phone number - 780-318-5062
• #22, 418 Maple Cres, St.Albert, Alberta.
• Our colours are black and green
Nice to have
• go wild i want something loud

```html
<!DOCTYPE html>
<html lang="en">
<head>
<meta charset="utf-8">
<title>Brightway Electric – Business Cards</title>
<link href="https://fonts.googleapis.com/css2?family=Arimo:wght@400;700&family=Archivo+Narrow:wght@400;600&display=swap" rel="stylesheet">
<style>
  :root {
    --stage: #3a3a3a;
    --card: #0a0e09;
    --card-edge: #1a2316;
    --green: #9bcb3c;
    --green-bright: #a6f01e;
    --green-glow: rgba(166, 240, 30, 0.55);
    --white: #f2f2f2;
  }
  * { margin: 0; padding: 0; box-sizing: border-box; }
  html, body {
    width: 1200px; height: 900px; overflow: hidden;
    background: radial-gradient(ellipse at 30% 20%, #5a5a5a 0%, var(--stage) 60%, #2a2a2a 100%);
    font-family: "Arimo", Arial, sans-serif;
  }
  .sheet {
    width: 1200px; height: 900px;
    display: flex; align-items: center; justify-content: center; gap: 40px;
  }
  .card {
    position: relative;
    width: 540px; height: 309px;
    background: var(--card);
    border: 1px solid var(--card-edge);
    box-shadow: 0 10px 30px rgba(0,0,0,0.45);
    overflow: hidden;
  }

  /* back: contact side */
  .card-back { color: var(--green); }
  .holder { position: absolute; left: 28px; top: 24px; font-size: 13px; line-height: 1.35; }
  .contact-list {
    position: absolute; left: 28px; top: 118px;
    list-style: none; font-size: 14px; line-height: 1;
  }
  .contact-list li { display: flex; align-items: center; gap: 6px; margin-bottom: 9px; }
  .contact-list svg { width: 14px; height: 14px; flex: none; }
  .mascot {
    position: absolute; right: 26px; top: 40px;
    width: 74px; height: 94px; border-radius: 38px 38px 20px 20px;
    background: linear-gradient(160deg, var(--green-bright) 0%, #dfe9d8 55%, #b9c7b2 100%);
  }
  .services {
    position: absolute; right: 18px; bottom: 18px;
    font-family: "Archivo Narrow", "Arial Narrow", sans-serif;
    font-size: 15px; color: var(--green-bright);
  }

  /* front: brand side */
  .card-front { display: flex; flex-direction: column; align-items: center; justify-content: center; gap: 30px; }
  .brand { display: flex; align-items: center; gap: 12px; }
  .brand-dot { width: 22px; height: 22px; border-radius: 50%; background: var(--green-bright); }
  .brand-name {
    font-family: "Arimo", Arial, sans-serif; font-weight: 700;
    font-size: 40px; color: var(--green-bright); text-transform: uppercase; letter-spacing: 1px;
  }
  .tagline {
    font-family: "Archivo Narrow", "Arial Narrow", sans-serif; font-weight: 600;
    font-size: 24px; color: var(--green-bright);
    text-shadow: 0 0 6px var(--green-glow), 0 0 14px var(--green-glow);
  }
</style>
</head>
<body>
<main class="sheet">
  <section class="card card-back">
    <div class="holder">
      <p class="holder-name">Your Name</p>
      <p class="holder-title">Title</p>
    </div>
    <ul class="contact-list">
      <li>
        <svg viewBox="0 0 14 14" aria-hidden="true"><path d="M7 1a4 4 0 0 0-4 4c0 3 4 8 4 8s4-5 4-8a4 4 0 0 0-4-4z" fill="none" stroke="currentColor" stroke-width="1.3"/><circle cx="7" cy="5" r="1.4" fill="currentColor"/></svg>
        #22, 418 Maple Cres, St. Albert, Alberta
      </li>
      <li>
        <svg viewBox="0 0 14 14" aria-hidden="true"><path d="M3 1.5h2l1 3-1.5 1a7 7 0 0 0 4 4l1-1.5 3 1v2A1.5 1.5 0 0 1 11 12.5 10 10 0 0 1 1.5 3 1.5 1.5 0 0 1 3 1.5z" fill="none" stroke="currentColor" stroke-width="1.2"/></svg>
        012-345-6789
      </li>
      <li>
        <svg viewBox="0 0 14 14" aria-hidden="true"><rect x="1.5" y="1.5" width="11" height="11" rx="2" fill="none" stroke="currentColor" stroke-width="1.2"/><path d="M4.5 4h1.3l.6 1.8-.9.6a4.5 4.5 0 0 0 2.1 2.1l.6-.9 1.8.6V9.5A1 1 0 0 1 9 10.5 6 6 0 0 1 3.5 5 1 1 0 0 1 4.5 4z" fill="currentColor"/></svg>
        780-318-5062
      </li>
    </ul>
    <div class="mascot" role="img" aria-label="Light bulb mascot character wearing a green cap"></div>
    <p class="services">"Commercial &amp; Residential Electrical Repair and Service"</p>
  </section>

  <section class="card card-front">
    <div class="brand">
      <span class="brand-dot" aria-hidden="true"></span>
      <span class="brand-name">Brightway Electric</span>
    </div>
    <p class="tagline">"your friendly neighbourhood electrician"</p>
  </section>
</main>
</body>
</html>
```